Web Design Project

We need a logo, web site and business cards for our new business, Velmora Vistas. We specialize in aerial videography and photography via drone. Currently we are mainly focusing on real estate videography but will branch into other markets and may even host training classes for flying drones.
Updates

Project Deadline Extended
Reason: The system set the deadline and it did not realize it was so short, sorry for the confusion!

Target Market(s)

Real estate agents, property managers, hotels and customers looking to learn how to fly drones.

Industry/Entity Type

Videography

Font styles to use
Sans Serif

Colors

Designer to choose colors to be used in the design.

Requirements
Must have
• Space for video feed on home page
A page for completed projects
A page for training classes
About us page

```html
<!DOCTYPE html>
<html lang="en">
<head>
<meta charset="utf-8">
<title>Velmora Vistas</title>
<link rel="stylesheet" href="https://fonts.googleapis.com/css2?family=PT+Sans:wght@400;700&family=Yanone+Kaffeesatz:wght@500;600;700&display=swap">
<style>
:root{
  --black:#000;
  --orange:#e8900f;
  --orange-deep:#c8690f;
  --orange-box:#b8660a;
  --dot-dim:#7a4f0a;
  --red:#c0161b;
  --red-bright:#d8190f;
  --white:#fff;
  --text:#f2f2f2;
  --grey:#9a9a9a;
  --frame:#3c3c3c;
  --tweet-bg:#2a1917;
  --icon:#4d4d4d;
}
*{margin:0;padding:0;box-sizing:border-box}
html,body{width:981px;height:1200px;overflow:hidden;background:var(--black)}
body{font-family:"PT Sans",Arial,sans-serif;color:var(--text)}
.page{position:relative;width:1200px;height:1468px;transform:scale(.8175);transform-origin:0 0;background:var(--black)}
.page > *{position:absolute}
.heading{font-family:"Yanone Kaffeesatz","Arial Narrow",sans-serif;font-weight:600;color:var(--white);font-size:40px;line-height:1}

/* header */
.site-header{left:0;top:0;width:1200px;height:186px;background:radial-gradient(ellipse 420px 120px at 600px 95px,#2a2a2a,#000 80%)}
.header-rule-top{left:0;top:0;width:1200px;height:7px;background:linear-gradient(90deg,#000,#bcbcbc 50%,#000)}
.header-rule-bottom{left:0;top:177px;width:1200px;height:9px;background:linear-gradient(90deg,#111,#d8d8d8 50%,#111)}
.brand{left:0;top:66px;width:1200px;display:flex;justify-content:center;align-items:center;gap:18px}
.brand-mark{width:44px;height:44px;background:var(--orange)}
.brand-name{font-family:"PT Sans",Arial,sans-serif;font-weight:700;font-size:52px;color:var(--white);letter-spacing:1px}

/* nav */
.main-nav{left:0;top:186px;width:1200px;height:51px;background:var(--orange)}
.main-nav a{position:absolute;top:0;height:51px;line-height:49px;font-size:23px;color:#1a1a1a;text-decoration:none}
.main-nav a.is-active{background:var(--black);color:var(--white);left:204px;width:111px;text-align:center}

/* hero */
.hero{left:89px;top:237px;width:1017px;height:310px;background:linear-gradient(#4a4a4a,#000)}
.video-feed{left:116px;top:257px;width:371px;height:246px;background:linear-gradient(180deg,#3a3530,#6b5a48 55%,#2d2620)}
.play-ring{left:221px;top:287px;width:132px;height:132px;border:5px solid var(--white);border-radius:50%}
.play-icon{left:278px;top:337px}
.trailer-label{left:116px;top:456px;width:371px;text-align:center;font-size:25px;letter-spacing:5px;color:#cfc8bd}
.slide-dots{left:238px;top:526px;display:flex;gap:12px}
.slide-dots span{width:20px;height:20px;background:var(--dot-dim)}
.slide-dots span.is-current{background:var(--orange)}
.hero-title{left:535px;top:283px;font-size:32px;color:var(--orange)}
.hero-copy{left:538px;top:329px;width:530px;font-size:20px;line-height:24px;color:var(--text)}
.btn-dark{left:888px;top:471px;width:199px;height:32px;background:var(--black);color:var(--white);font-size:15px;text-align:center;line-height:32px}

/* gallery */
.gallery-title{left:107px;top:617px}
.arrow{width:29px;height:29px;background:var(--red);display:flex;align-items:center;justify-content:center}
.gallery-prev{left:509px;top:625px}
.gallery-next{left:549px;top:625px}
.gallery-frame{left:92px;top:686px;width:506px;height:259px;background:var(--orange-deep)}
.gallery-photo{left:106px;top:702px;width:477px;height:226px;background:linear-gradient(90deg,#c79a76,#d9e7f0 45%,#c7e2f7)}

/* classes */
.classes-title{left:107px;top:979px}
.class-thumb{left:89px;top:1053px;width:123px;height:109px;background:linear-gradient(135deg,#7a2d22,#b5563f 50%,#5b211b)}
.class-tag{left:236px;top:1048px;width:205px;height:21px;background:var(--orange);color:#1a1a1a;font-size:17px;line-height:21px;padding-left:7px}
.class-copy{left:236px;top:1075px;width:280px;font-size:17.5px;line-height:21.5px}
.class-more{left:236px;top:1144px;font-size:15.5px}

/* news */
.news-title{left:664px;top:622px}
.news-frame{width:162px;height:132px;background:var(--frame)}
.news-photo{width:137px;height:102px;border:1px solid var(--white)}
.news-copy{left:845px;width:270px;font-size:17.5px;line-height:21.5px}
.news-more{left:847px;font-size:15.5px}

/* newsletter */
.newsletter{left:660px;top:1048px;width:446px;height:138px;background:var(--orange-box)}
.newsletter-title{left:687px;top:1066px}
.newsletter-input{left:687px;top:1124px;width:270px;height:41px;background:var(--black)}
.btn-subscribe{left:966px;top:1124px;width:126px;height:39px;background:var(--red-bright);color:var(--white);font-size:18px;text-align:center;line-height:39px}

/* tweet bar */
.tweet-bar{left:0;top:1224px;width:1200px;height:90px;background:var(--tweet-bg)}
.tweet-badge{left:110px;top:1246px;width:50px;height:50px;border-radius:50%;background:var(--white)}
.tweet-text{left:185px;top:1263px;font-size:17px;color:var(--white)}
.tweet-prev{left:1027px;top:1224px}
.tweet-next{left:1067px;top:1224px}
.accent-band{left:0;top:1316px;width:1200px;height:46px;background:var(--orange-deep)}

/* footer */
.site-footer{left:0;top:1362px;width:1200px;height:106px;background:var(--black)}
.footer-brand{left:120px;top:1393px;display:flex;align-items:center;gap:9px}
.footer-brand .brand-mark{width:20px;height:20px}
.footer-brand .brand-name{font-size:24px;letter-spacing:.5px}
.copyright{left:343px;top:1385px;font-size:17px;color:var(--grey)}
.legal{left:344px;top:1415px;font-size:17px;color:var(--grey)}
.social{left:756px;top:1392px;display:flex;gap:7px}
.social span{width:36px;height:36px;border-radius:50%;background:var(--icon);display:flex;align-items:center;justify-content:center}
</style>
</head>
<body>
<div class="page">
  <header class="site-header"></header>
  <div class="header-rule-top"></div>
  <div class="brand"><span class="brand-mark"></span><span class="brand-name">VELMORA VISTAS</span></div>
  <div class="header-rule-bottom"></div>

  <nav class="main-nav">
    <a class="is-active" href="#">Home</a>
    <a href="#" style="left:344px">About</a>
    <a href="#" style="left:457px">Photos</a>
    <a href="#" style="left:578px">Videos</a>
    <a href="#" style="left:695px">Classes</a>
    <a href="#" style="left:818px">Contact</a>
  </nav>

  <section class="hero"></section>
  <div class="video-feed" role="img" aria-label="Video still of a figure walking down a misty corridor"></div>
  <div class="play-ring"></div>
  <svg class="play-icon" width="28" height="32" viewBox="0 0 28 32"><polygon points="0,0 28,16 0,32" fill="#fff"/></svg>
  <div class="trailer-label">TRAILER</div>
  <div class="slide-dots"><span class="is-current"></span><span></span><span></span><span></span><span></span></div>
  <h1 class="heading hero-title">Specialize in aerial videography and photography</h1>
  <p class="hero-copy">Your best resource for everything related to the most explosive and dynamic rising star of action cinema. With exclusive news, videos, galleries and fitness advice from the man himself, make sure you sign up to our newsletter. Enjoy the site and come back soon.</p>
  <div class="btn-dark">Read more about us</div>

  <h2 class="heading gallery-title">Photo Gallery</h2>
  <div class="arrow gallery-prev"><svg width="10" height="16" viewBox="0 0 10 16"><polyline points="8,1 2,8 8,15" fill="none" stroke="#fff" stroke-width="2"/></svg></div>
  <div class="arrow gallery-next"><svg width="10" height="16" viewBox="0 0 10 16"><polyline points="2,1 8,8 2,15" fill="none" stroke="#fff" stroke-width="2"/></svg></div>
  <div class="gallery-frame"></div>
  <div class="gallery-photo" role="img" aria-label="Photo of a photographer in a sun hat taking a picture against a blue sky"></div>

  <h2 class="heading classes-title">Training Classes</h2>
  <div class="class-thumb" role="img" aria-label="Photo of a performer with a guitar on stage"></div>
  <div class="class-tag">New Bach Start Soon</div>
  <p class="class-copy">Your best resource for everything related to the most explosive and cinema.</p>
  <div class="class-more">Read more</div>

  <h2 class="heading news-title">Latest News Post</h2>
  <div class="news-frame" style="left:663px;top:685px"></div>
  <div class="news-photo" role="img" aria-label="Photo of two people on a film set" style="left:676px;top:699px;background:linear-gradient(135deg,#6b2a1a,#c06040 50%,#3a1a14)"></div>
  <p class="news-copy" style="top:687px">Your best resource for everything related to the most explosive and dynamic rising star of action cinema.</p>
  <div class="news-more" style="top:800px">Read more</div>
  <div class="news-frame" style="left:663px;top:857px"></div>
  <div class="news-photo" role="img" aria-label="Photo of a singer with a guitar on stage" style="left:676px;top:873px;background:linear-gradient(135deg,#5a1f18,#a8503a 50%,#4a1a14)"></div>
  <p class="news-copy" style="top:858px">Your best resource for everything related to the most explosive and dynamic rising star of action cinema.</p>
  <div class="news-more" style="top:971px">Read more</div>

  <div class="newsletter"></div>
  <h2 class="heading newsletter-title">Email Newsletter</h2>
  <div class="newsletter-input"></div>
  <div class="btn-subscribe">Subscribe</div>

  <div class="tweet-bar"></div>
  <div class="tweet-badge"></div>
  <p class="tweet-text">@Discover who Dara Holloway is and why so many “big names” listen to her, and how Brightlane Outreach ...</p>
  <div class="arrow tweet-prev"><svg width="10" height="16" viewBox="0 0 10 16"><polyline points="8,1 2,8 8,15" fill="none" stroke="#fff" stroke-width="2"/></svg></div>
  <div class="arrow tweet-next"><svg width="10" height="16" viewBox="0 0 10 16"><polyline points="2,1 8,8 2,15" fill="none" stroke="#fff" stroke-width="2"/></svg></div>
  <div class="accent-band"></div>

  <footer class="site-footer"></footer>
  <div class="footer-brand"><span class="brand-mark"></span><span class="brand-name">VELMORA VISTAS</span></div>
  <p class="copyright">Copyright &copy; 2014</p>
  <p class="legal">Privacy Policy | &nbsp;Legal Notices</p>
  <div class="social">
    <span></span><span></span><span></span><span></span><span></span>
    <span><svg width="20" height="14" viewBox="0 0 20 14"><rect x="1" y="1" width="18" height="12" fill="none" stroke="#111" stroke-width="2"/><polyline points="1,1 10,8 19,1" fill="none" stroke="#111" stroke-width="2"/></svg></span>
  </div>
</div>
</body>
</html>
```